Football (soccer) board game app design

Hi,

We are a start up looking for a gameplay design for an app. It is a football trivia app that consists of four main screens; login/register, main navigation, gameplay, question.

OVERALL:
We want our app to be kept in a dark theme. Black or very dark gray is preferable, with a couple of nice colors to give it a stylish touch. We like flat designs, but are open for ideas within the general structure design. The logo can be used in the app, but feel free to improve it you feel you can. In the attached material we have tried to outline some of our ideas and other designs friends have helped us make.

LOGIN/REGISTER:
We want a simple login. Email, password, Chatterly login and the possibility to register a new user. Live search check whether the email is valid and free, and there is also live validation of passwords. If this could be incorporated in the design it would be nice.

MAIN NAVIGATION:
In the main navigation screen we want it to be divided into tabs. A home, my games, my categories and a ranking tab. In the top bar it should be possible to search for categories as well as there should be a button to go to settings.

The Home tab
In the home tab we want a "Quick Play" button, and a list of featured categories. A category can be unlocked or locked, which should be illustrated somehow. When a category is tapped it should divide the block into a left and right tap area, where the user can choose to "Beat to unlock" or "Buy to unlock" if locked and "Practice" or "Challenge Friend" if already unlocked.

The My Games tab
In the my games tab, the current games should be divided into three lists. First "your turn", then "opponents turn" and finally "finished games".

The My Categories tab
This tab should include a list of categories, which the user have bought, but as of design it is fairly similar to the blocks in home tab. So not much different here.

The Ranking tab
Ranking should show a set of leaderboards; Today, This Week, This Month, etc. The row in a leaderboard should have teamname and a win percentage.

GAMEPLAY:
The gameplay is inspired by an old football (soccer) board game from the 1950's, and our gameplay consists of three core elements; a football (soccer) pitch, 11 players and a scoreboard.

The football (soccer) pitch
What we need is a pitch seen from behind the goal line. The important issue here, is the perspective, as we want 11 players on the field formed as a 4-3-3 formation, being 1 goalkeeper, 4 defenders, 3 midfielder and 3 strikers. They should all be touchable without overlap. In the other end we want a goal that should be touchable as well. The goal in the nearest end do not have to be visible. Due to the perspective of the field and the fact that players and goal should be touchable, of course give you the opportunity to play around with the proportions of both players and goal. We rather want a large goal being out of proportions, than a small goal with a tiny tap area. Around the field (sidelines and beside the goal) we would like advertising banners like seen on a real stadium.

The players
As mentioned we want 11 players in a 4-3-3 formation. The players should be attached to the board with springs as seen on some of the very old board games, where you could flick the player to pass the ball. This also means that we want the players to be placed in an indentation for the ball to fall into and it would be very cool if you could illustrate the player with the ball, as being pulled back to one of the sides, just enough to see the ball at his feet. The players should be large enough for a user to tap them, hence it would also be beneficial if they are not overlapping. For a start we would like to see the players in a blue shirt and white shorts (socks are not necessary as they are placed on a spring).

Scoreboard
On the scoreboard above the field, we need information such as the names of the two teams (could be FC Brightmoor and Tall Oak Rovers), the score (2-1), minutes played (42), and which half (1st). We also want a progress bar that illustrates how many moves you have used ranging from 0-5. The scoreboard could be inspired from the ones seen around stadiums across the world, but feel free to improvise.

What We Are Looking for
We are looking for full PSD and AI files so we can use them to make minor changes like colors on shirts and shorts, colors on pitch, etc. We really want you to be innovative and inspire us, as we are not designers ourselves. In the attached files, we have tried to sketch out a design that covers our initial ideas. We are looking for a professional look, and having the players and field look like a real board game would just be awesome. A combination of the look from the realistic pitch with advertising banners around it, the idea of our spring-players and the initial thoughts of a design illustrated in our sketch, should help you along. Flat design, cartoonish or somewhere in between is up to you, we just want you to impress and make "wow"-feeling.

QUESTION:
The final screen should display a question with four possible answers. There should be a green/checkmark when correct answer, and a red/cross if incorrect.

That's all. We are looking very much forward to see your designs!
Updates

Hi all,

We have changed the terms of the contest to now have a guaranteed payment, and we are really looking forward to see your designs! Good luck.

/ Mikkel and Anders

By request we have now uploaded an AI-file with the logo for you to play around with. We are looking forward to see your designs.

/ Mikkel and Anders

Reason: Hi designers, We are really happy with the progress being made, and are looking forward to see some of the designs that are still work in progress. However the amount of designs received, has not reached our expectations yet. Therefore we are extending the deadline for seven more days, so designers, that are still working on their designs can continue their work without a stressing deadline in the horizon. Good luck to all of you. We are looking very much forward to see, what you are able to produce. Best regards, Mikkel and Anders

Reason: Hi all, We still have a lot of designers in the competition , who are battling to finish their designs, therefore we have decided to extend the deadline once more. Good luck to all of you!

Target Market(s)

Football (soccer) fans

Industry/Entity Type

Advertising

```html
<!DOCTYPE html>
<html lang="en">
<head>
<meta charset="utf-8">
<title>kickwise – main navigation tabs</title>
<link rel="stylesheet" href="https://fonts.googleapis.com/css2?family=Quicksand:wght@300;400&display=swap">
<style>
  :root {
    --canvas-bg: #ffffff;
    --screen-dark: #231f20;
    --screen-blue: #1b6f9e;
    --screen-cyan: #12b3d6;
    --icon-white: #ffffff;
    --pill-light: #8f9a9f;
    --pill-dark: #3a4a52;
    --note-ink: #3a3a3a;
  }
  * { margin: 0; padding: 0; box-sizing: border-box; }
  html, body {
    width: 1200px; height: 328px; overflow: hidden;
    background: var(--canvas-bg);
  }
  .canvas { position: relative; width: 1200px; height: 328px; }

  .app-screen {
    position: absolute; left: 32px; top: 25px; width: 647px; height: 303px;
    overflow: hidden;
    background:
      radial-gradient(ellipse 320px 120px at 560px 0px, var(--screen-cyan) 0%, rgba(18,179,214,0) 100%),
      linear-gradient(180deg, var(--screen-blue) 0%, #174a66 30%, #1d2f38 58%, var(--screen-dark) 82%);
  }
  .brand-name {
    position: absolute; left: 0; right: 0; top: 0;
    text-align: center;
    font-family: "Quicksand", sans-serif; font-weight: 300;
    font-size: 44px; letter-spacing: 1px; line-height: 1;
    color: var(--icon-white);
    padding-top: 8px;
  }
  .tab-bar {
    position: absolute; left: 13px; top: 89px; width: 621px; height: 71px;
    border: 3.5px solid var(--icon-white); border-radius: 32px;
  }
  .tab {
    position: absolute; top: 50%; width: 52px; height: 52px;
    transform: translate(-50%, -50%);
    display: flex; align-items: center; justify-content: center;
  }
  .tab svg { width: 52px; height: 52px; display: block; }
  .tab--home { left: 56px; }
  .tab--games { left: 161px; }
  .tab--categories { left: 264px; }
  .tab--ranking { left: 368px; }
  .tab--search { left: 470px; }
  .tab--settings { left: 572px; }
  .tab--selected::before {
    content: ""; position: absolute; left: 50%; top: 50%;
    width: 94px; height: 56px; transform: translate(-50%, -50%);
    border-radius: 28px;
    background: linear-gradient(180deg, var(--pill-light) 0%, var(--pill-dark) 100%);
    opacity: 0.85;
  }
  .tab--selected svg { position: relative; }

  .notes {
    position: absolute; left: 760px; top: 26px; width: 292px;
    text-align: center;
    font-family: "Quicksand", sans-serif; font-weight: 400;
    font-size: 23px; line-height: 38px; color: var(--note-ink);
  }
  .notes p + p { margin-top: 39px; }
</style>
</head>
<body>
<div class="canvas">
  <section class="app-screen">
    <div class="brand-name">kickwise</div>
    <nav class="tab-bar">
      <div class="tab tab--home" aria-label="Home">
        <svg viewBox="0 0 52 52" fill="var(--icon-white)">
          <path d="M26 5 L3 26 L8 26 L26 10 L44 26 L49 26 Z"/>
          <path d="M11 27 L26 14 L41 27 L41 46 L31 46 L31 33 L21 33 L21 46 L11 46 Z"/>
          <rect x="36" y="9" width="5" height="10"/>
        </svg>
      </div>
      <div class="tab tab--games tab--selected" aria-label="My Games">
        <svg viewBox="0 0 52 52">
          <circle cx="26" cy="26" r="21" fill="var(--icon-white)" stroke="#222" stroke-width="1.5"/>
          <polygon points="26,19 33,24 30,32 22,32 19,24" fill="#1a1a1a"/>
          <path d="M26 5 L26 19 M33 24 L45 20 M30 32 L37 43 M22 32 L15 43 M19 24 L7 20" stroke="#1a1a1a" stroke-width="1.5"/>
          <path d="M20 6 L26 5 L32 6 L26 10 Z M44 14 L46 22 L43 27 L41 20 Z M8 14 L6 22 L9 27 L11 20 Z M17 45 L25 47 L33 45 L28 41 L23 41 Z" fill="#1a1a1a"/>
        </svg>
      </div>
      <div class="tab tab--categories" aria-label="Categories">
        <svg viewBox="0 0 52 52" fill="var(--icon-white)">
          <rect x="3" y="8" width="9" height="9"/><rect x="15" y="8" width="34" height="9"/>
          <rect x="3" y="21" width="9" height="9"/><rect x="15" y="21" width="34" height="9"/>
          <rect x="3" y="34" width="9" height="9"/><rect x="15" y="34" width="34" height="9"/>
        </svg>
      </div>
      <div class="tab tab--ranking" aria-label="Ranking">
        <svg viewBox="0 0 52 52" fill="var(--icon-white)">
          <path d="M17 27 L9 48 L15 44 L18 50 L24 33 Z"/>
          <path d="M35 27 L43 48 L37 44 L34 50 L28 33 Z"/>
          <circle cx="26" cy="17" r="14"/>
          <circle cx="26" cy="17" r="10" fill="none" stroke="#1d3a4a" stroke-width="1.6"/>
          <polygon points="26,10 28,15 33,15 29,18 30.5,23 26,20 21.5,23 23,18 19,15 24,15" fill="#1d3a4a"/>
        </svg>
      </div>
      <div class="tab tab--search" aria-label="Search">
        <svg viewBox="0 0 52 52">
          <circle cx="21" cy="20" r="13" fill="none" stroke="var(--icon-white)" stroke-width="6"/>
          <path d="M30 30 L46 45" stroke="var(--icon-white)" stroke-width="8" stroke-linecap="round"/>
        </svg>
      </div>
      <div class="tab tab--settings" aria-label="Settings">
        <svg viewBox="0 0 52 52">
          <g fill="var(--icon-white)" transform="translate(26 26)">
            <circle r="15"/>
            <rect x="-4.5" y="-22" width="9" height="10"/>
            <rect x="-4.5" y="-22" width="9" height="10" transform="rotate(45)"/>
            <rect x="-4.5" y="-22" width="9" height="10" transform="rotate(90)"/>
            <rect x="-4.5" y="-22" width="9" height="10" transform="rotate(135)"/>
            <rect x="-4.5" y="-22" width="9" height="10" transform="rotate(180)"/>
            <rect x="-4.5" y="-22" width="9" height="10" transform="rotate(225)"/>
            <rect x="-4.5" y="-22" width="9" height="10" transform="rotate(270)"/>
            <rect x="-4.5" y="-22" width="9" height="10" transform="rotate(315)"/>
          </g>
          <circle cx="26" cy="26" r="6" fill="#203038"/>
        </svg>
      </div>
    </nav>
  </section>

  <aside class="notes">
    <p>Home- MyGames- Categories<br>Ranking - Search - Settings</p>
    <p>The icons represent the tabs.</p>
    <p>My Games Tab is selected</p>
  </aside>
</div>
</body>
</html>
```